Tech Company requires UI design for mobile app

We need a mobile app design for a company based in Singapore called "Kalvor Systems". We develop innovative Android/iOS business applications. KalvorLink - a collaboration tool targeted at SMEs that improves reporting and communication between different departments of an organisation. We would like to see designs that use the colour orange, our corporate colour. The final design should communicate clean and technology inclined design.

You are expected to recreate the icons, layout and structure without affecting the workflow.This is a workplace app for employee on mobile. The mobile app aims to empower individual employee to complete the following processes:

1. HR processes - taking attendance, timesheet, employment management to payslip)
2. Inventory management - stock taking, gift redemption and real-time stock management
3. Digital form - application for inspection, safety, procurement or request creation)
4. Job - an app that allows web portal to assign work to individual worker.
Updates

Reason: Received feedback to extens timeline. Cheers!

Target Market(s)

C-Executive, office employee, retail promoter, worker

Industry/Entity Type

Business

Colors

Designer to choose colors to be used in the design.

Requirements
Must have
• - Design must be neat, looks professional and perceived to be user-friendly
• - Use colour theme for each category
• - Must complement with KalvorLink logo them (already attached)
• - Have "apple" feel
• - We like the layout reference 1 & reference 2 photo. However, we prefer a better colour theme (Already Attached)
• - Please download the link for the work required
• https://files.quillbox.example/open?id=7Hq2LmPzXw9RtNc4VbKjYs8DfGaTe3Uo
Nice to have
• More info to follow shortly
Should not have
• - Must not be loud, flashy, dull, bored,
• - Design should not clash with Kalvor Link Logo
• -

```html
<!DOCTYPE html>
<html lang="en">
<head>
<meta charset="utf-8">
<title>KalvorLink – Mobile App Screens</title>
<link href="https://fonts.googleapis.com/css2?family=Roboto:wght@300;400;500&display=swap" rel="stylesheet">
<style>
:root{
  --purple-top:#8a2fe2;
  --purple-mid:#7d4fe0;
  --purple-low:#7464de;
  --purple-soft:#8c82dc;
  --text-dark:#333;
  --text-mid:#666;
  --text-light:#999;
  --line:#e3e3e3;
  --page:#ffffff;
  --sky:#5ac8fa;
  --confirm:#5ac8fa;
  --in:#ff2d55;
  --out:#4cd964;
}
*{box-sizing:border-box;margin:0;padding:0}
html,body{width:1120px;height:1200px;overflow:hidden;background:var(--page)}
body{font-family:"Roboto",sans-serif;color:var(--text-dark)}
.board{width:1400px;height:1500px;transform:scale(.8);transform-origin:0 0;position:relative}
.screen{position:absolute;width:375px;height:667px;overflow:hidden;background:#fff;box-shadow:0 2px 14px rgba(0,0,0,.10)}
.s1{left:60px;top:49px;background:linear-gradient(#f6f6fb,#fff)}
.s2{left:512px;top:49px}
.s3{left:963px;top:49px}
.s4{left:60px;top:772px}
.s5{left:512px;top:772px;background:linear-gradient(var(--purple-top),var(--purple-low))}
.s6{left:963px;top:772px}
.abs{position:absolute}
.status{position:absolute;left:0;top:0;width:375px;height:22px;font-size:12px;color:#fff}
.status.dark{color:#000}
.status .carrier{position:absolute;left:7px;top:4px}
.status .time{position:absolute;left:0;right:0;top:5px;text-align:center}
.status .batt{position:absolute;right:8px;top:4px;display:flex;align-items:center;gap:4px}
.status .batt i{display:inline-block;width:20px;height:9px;border:1px solid currentColor;border-radius:2px;position:relative}
.status .batt i::after{content:"";position:absolute;inset:1px;background:currentColor}
.appbar{position:absolute;left:0;top:0;width:375px;height:72px;background:var(--purple-top);border-bottom:1px solid rgba(255,255,255,.25)}
.appbar .title{position:absolute;left:0;right:0;top:41px;text-align:center;color:#fff;font-size:21px;font-weight:400}
.appbar .title.left{left:8px;text-align:left;font-size:23px}
.appbar svg{position:absolute;top:43px}
.profile{position:absolute;left:0;top:72px;width:375px;height:116px;background:linear-gradient(var(--purple-mid),var(--purple-low))}
.avatar{position:absolute;left:17px;top:20px;width:72px;height:72px;border-radius:50%;border:3px solid rgba(255,255,255,.5);background:linear-gradient(135deg,#d8c8b8,#6e5a50)}
.profile .name{position:absolute;left:104px;top:34px;color:#fff;font-size:20px}
.profile .code{position:absolute;left:104px;top:62px;color:rgba(255,255,255,.85);font-size:15px}
/* login */
.brand{position:absolute;left:0;right:0;top:182px;display:flex;justify-content:center;align-items:center;gap:10px;font-size:42px;font-weight:300;color:#444}
.brand .dot{width:30px;height:30px;border-radius:50%;background:#f36f21}
.field{position:absolute;left:42px;width:292px;height:44px;border:1px solid #dcdcdc;background:#fff;padding:13px 16px;font-size:15px;color:#888}
.btn-login{position:absolute;left:42px;top:467px;width:292px;height:44px;background:var(--purple-soft);color:#fff;font-size:19px;text-align:center;line-height:44px;font-weight:300}
.center-text{position:absolute;left:0;right:0;text-align:center;font-size:15px;color:var(--text-mid)}
.center-text a{color:#1a73e8;text-decoration:none}
/* dashboard */
.section-title{position:absolute;left:0;right:0;text-align:center;font-size:19px;color:#888;font-weight:300}
.grid{position:absolute;left:0;width:375px;display:flex}
.tile{width:96px;display:flex;flex-direction:column;align-items:center;font-size:13.5px;color:#888;text-align:center;line-height:17px}
.tile .ic{width:40px;height:40px;border-radius:50%;display:flex;align-items:center;justify-content:center;margin-bottom:8px}
.tile .ic svg{width:22px;height:22px;fill:none;stroke:#fff;stroke-width:2;stroke-linecap:round;stroke-linejoin:round}
.divider{position:absolute;left:0;width:375px;height:5px;background:#f0f0f0}
.bottomnav{position:absolute;left:0;top:597px;width:375px;height:70px;border-top:1px solid var(--line);display:flex;justify-content:space-around;align-items:center}
.bottomnav svg{width:22px;height:22px;fill:none;stroke:#aaa;stroke-width:1.6}
/* map screens */
.map{position:absolute;left:0;top:180px;width:375px;height:487px;background:linear-gradient(160deg,#f4efe6 0%,#e9e4da 35%,#7fb8e8 55%,#d7ecd0 80%,#f2eee6 100%)}
.map.faded{opacity:.35}
.info{position:absolute;left:10px;top:324px;width:355px;height:270px;background:rgba(122,84,224,.93);color:#fff;font-size:16px}
.info .row{position:absolute;left:0;width:355px}
.info .k{position:absolute;right:245px;text-align:right;white-space:nowrap}
.info .v{position:absolute;left:133px;font-weight:500;line-height:22px}
.locate{position:absolute;left:321px;top:276px;width:42px;height:42px;border-radius:50%;background:var(--sky);display:flex;align-items:center;justify-content:center}
.round{position:absolute;width:46px;height:46px;border-radius:50%;color:#fff;font-size:21px;text-align:center;line-height:44px}
.dialog{position:absolute;left:10px;top:355px;width:355px;height:157px;background:#fff;border:1px solid #f0d6f2;box-shadow:0 2px 10px rgba(0,0,0,.08)}
.dialog h3{position:absolute;left:0;right:0;top:16px;text-align:center;font-weight:400;font-size:21px;color:#222}
.dialog p{position:absolute;left:0;right:0;top:64px;text-align:center;font-size:16px;color:#444}
.dbtn{position:absolute;top:105px;width:155px;height:40px;line-height:40px;text-align:center;font-size:20px;font-weight:300}
.dbtn.cancel{left:15px;background:#e6e6e6;color:#555}
.dbtn.ok{left:185px;background:var(--confirm);color:#fff}
/* calendar */
.monthbar{position:absolute;left:0;top:90px;width:375px;height:24px;color:#fff;font-size:18px}
.cal{position:absolute;left:0;top:134px;width:375px;display:grid;grid-template-columns:repeat(7,1fr);grid-auto-rows:51px;color:#fff;font-size:17px}
.cal > span{display:flex;align-items:center;justify-content:center;position:relative}
.cal .sel::before{content:"";position:absolute;left:50%;top:50%;width:56px;height:56px;margin:-28px 0 0 -28px;border-radius:50%;background:rgba(255,255,255,.18);border:2px solid rgba(255,255,255,.35)}
.cal .sel b{position:relative;font-weight:400}
.cal .wk{font-weight:500}
.event{position:absolute;left:14px;width:348px;height:68px;background:#fff;padding:10px 14px}
.event .t{font-size:17px;color:#888}
.event .s{font-size:13px;color:#999;margin-top:6px}
.event .h{position:absolute;right:14px;top:12px;font-size:15px;color:#888}
/* projects */
.filterbar{position:absolute;left:0;top:72px;width:375px;height:58px;background:var(--purple-low);color:#fff;font-size:16px}
.acc{position:absolute;left:11px;width:353px;height:44px;border:1px solid var(--line);padding:11px 14px;font-size:17px;color:#999;background:#fff}
.acc svg{position:absolute;right:12px;top:16px}
.detail{position:absolute;left:21px;top:185px;width:333px;height:196px;border:1px solid var(--line);border-top:none;font-size:15px;color:#555}
.detail .line{position:absolute;left:58px;display:flex;gap:10px;align-items:flex-start}
.detail svg{width:20px;height:20px;fill:none;stroke:#4a8fe8;stroke-width:1.6;flex:none}
.fab{position:absolute;left:161px;top:588px;width:54px;height:54px;border-radius:50%;background:#fff;box-shadow:0 2px 10px rgba(0,0,0,.15);display:flex;align-items:center;justify-content:center}
</style>
</head>
<body>
<div class="board">

<!-- Login -->
<section class="screen s1">
  <div class="status dark"><span class="carrier">●●●● Carrier</span><span class="time">9:41 AM</span><span class="batt">100% <i></i></span></div>
  <div class="brand"><span class="dot"></span>Kalvor</div>
  <div class="field" style="top:286px">Username</div>
  <div class="field" style="top:346px">Password</div>
  <div class="btn-login">Login</div>
  <div class="center-text" style="top:522px">Don't have an account? <a href="#">Register Now</a></div>
  <div class="center-text" style="top:629px">Forgot Password?</div>
</section>

<!-- Dashboard -->
<section class="screen s2">
  <div class="appbar">
    <div class="status"><span class="carrier">●●●● Carrier</span><span class="time">9:41 AM</span><span class="batt">100% <i></i></span></div>
    <div class="title left">KalvorLink</div>
    <svg style="left:300px" width="22" height="22" viewBox="0 0 24 24" fill="none" stroke="#fff" stroke-width="1.8"><path d="M6 17V11a6 6 0 0 1 12 0v6l2 2H4z"/><path d="M10 21h4"/><circle cx="20" cy="4" r="3" fill="#ffa726" stroke="none"/></svg>
    <svg style="left:338px" width="22" height="22" viewBox="0 0 24 24" fill="none" stroke="#fff" stroke-width="1.8"><circle cx="12" cy="12" r="3.5"/><circle cx="12" cy="12" r="8" stroke-dasharray="4 2.3"/></svg>
  </div>
  <div class="profile"><div class="avatar" role="img" aria-label="Employee profile photo"></div><div class="name">Mara Quinlan</div><div class="code">EM12456</div></div>

  <div class="section-title" style="top:210px">Attendence</div>
  <div class="grid" style="top:250px;left:-1px">
    <div class="tile"><div class="ic" style="background:#8a7ee0"><svg viewBox="0 0 24 24"><path d="M12 21s-7-6-7-11a7 7 0 0 1 14 0c0 5-7 11-7 11z"/><circle cx="12" cy="10" r="2.5"/></svg></div>Take<br>Attendence</div>
    <div class="tile"><div class="ic" style="background:#4fc3f7"><svg viewBox="0 0 24 24"><circle cx="12" cy="12" r="8"/><path d="M12 8v4l3 2"/></svg></div>Today</div>
    <div class="tile"><div class="ic" style="background:#5a4fd8"><svg viewBox="0 0 24 24"><path d="M6 3h8l4 4v14H6z"/><path d="M9 12h6M9 16h6"/></svg></div>Past Records</div>
    <div class="tile"><div class="ic" style="background:#8c5ce0"><svg viewBox="0 0 24 24"><circle cx="9" cy="8" r="3"/><path d="M3 19a6 6 0 0 1 12 0z"/><path d="M16 5a3 3 0 0 1 0 6M18 14a5 5 0 0 1 3 5"/></svg></div>Stations</div>
  </div>
  <div class="divider" style="top:336px"></div>

  <div class="section-title" style="top:358px">Sales &amp; Inventory</div>
  <div class="grid" style="top:398px;left:-1px">
    <div class="tile"><div class="ic" style="background:#ffa726"><svg viewBox="0 0 24 24"><path d="M12 3l8 4v10l-8 4-8-4V7z"/><path d="M4 7l8 4 8-4M12 11v10"/></svg></div>New<br>Redemtion</div>
    <div class="tile"><div class="ic" style="background:#ffd21f"><svg viewBox="0 0 24 24"><path d="M2 12s4-6 10-6 10 6 10 6-4 6-10 6S2 12 2 12z"/><circle cx="12" cy="12" r="2.5"/></svg></div>View<br>Redemtion</div>
    <div class="tile"><div class="ic" style="background:#4cd964"><svg viewBox="0 0 24 24"><path d="M4 8h4l2-2h4l2 2h4v11H4z"/><circle cx="12" cy="13" r="3"/></svg></div>Take<br>Photo</div>
    <div class="tile"><div class="ic" style="background:#ff3b5c"><svg viewBox="0 0 24 24"><path d="M3 17l6-6 4 4 8-8"/><path d="M15 7h6v6"/></svg></div>Sales<br>Summary</div>
  </div>
  <div class="grid" style="top:499px;left:-1px">
    <div class="tile"><div class="ic" style="background:#f5702b"><svg viewBox="0 0 24 24"><circle cx="12" cy="12" r="8"/><path d="M8 12l3 3 5-6"/></svg></div>Inventory<br>Check</div>
    <div class="tile"><div class="ic" style="background:#3a8ab0"><svg viewBox="0 0 24 24"><path d="M3 5h3l2 10h10l2-7H7"/><circle cx="9" cy="19" r="1.4"/><circle cx="17" cy="19" r="1.4"/></svg></div>Delivery</div>
    <div class="tile"><div class="ic" style="background:#14a89a"><svg viewBox="0 0 24 24"><path d="M3 12V4h8l10 10-7 7z"/><circle cx="7.5" cy="8" r="1.3"/></svg></div>New Stock<br>Take</div>
    <div class="tile"><div class="ic" style="background:#7ed321"><svg viewBox="0 0 24 24"><rect x="6" y="5" width="12" height="16" rx="1"/><path d="M9 3h6v4H9z"/></svg></div>Stock Take<br>List</div>
  </div>

  <div class="bottomnav">
    <svg viewBox="0 0 24 24"><path d="M4 11l8-7 8 7v10H4z"/><path d="M10 21v-5h4v5"/></svg>
    <svg viewBox="0 0 24 24"><circle cx="12" cy="8" r="4"/><path d="M4 21a8 8 0 0 1 16 0"/></svg>
    <svg viewBox="0 0 24 24"><rect x="4" y="5" width="16" height="16"/><path d="M4 10h16M8 3v4M16 3v4"/></svg>
    <svg viewBox="0 0 24 24"><path d="M20 11a8 8 0 0 0-14-5l-2 2M4 13a8 8 0 0 0 14 5l2-2"/><path d="M4 4v4h4M20 20v-4h-4"/></svg>
  </div>
</section>

<!-- Attendance map -->
<section class="screen s3">
  <div class="map" role="img" aria-label="Street map around the employee's current location"></div>
  <div class="appbar">
    <div class="status"><span class="carrier">●●●● Carrier</span><span class="time">9:41 AM</span><span class="batt">100% <i></i></span></div>
    <svg style="left:8px" width="22" height="22" viewBox="0 0 24 24" fill="none" stroke="#fff" stroke-width="2"><path d="M20 12H4M10 6l-6 6 6 6"/></svg>
    <div class="title">Attendence</div>
    <svg style="left:338px" width="22" height="22" viewBox="0 0 24 24" fill="none" stroke="#fff" stroke-width="1.8"><circle cx="12" cy="12" r="3.5"/><circle cx="12" cy="12" r="8" stroke-dasharray="4 2.3"/></svg>
  </div>
  <div class="profile"><div class="avatar" role="img" aria-label="Employee profile photo"></div><div class="name">Mara Quinlan</div><div class="code">EM12456</div></div>
  <svg class="abs" style="left:118px;top:214px" width="38" height="48" viewBox="0 0 24 30" fill="#fff" stroke="#7d4fe0" stroke-width="1.6"><path d="M12 28S3 18 3 11a9 9 0 0 1 18 0c0 7-9 17-9 17z"/><circle cx="12" cy="11" r="3.5"/></svg>
  <div class="locate"><svg width="24" height="24" viewBox="0 0 24 24" fill="none" stroke="#fff" stroke-width="1.8"><circle cx="12" cy="12" r="7"/><circle cx="12" cy="12" r="2.5"/><path d="M12 2v4M12 18v4M2 12h4M18 12h4"/></svg></div>
  <div class="info">
    <div class="row" style="top:18px"><span class="k">Location:</span><span class="v">Harbor Bridge</span></div>
    <div class="row" style="top:66px"><span class="k">Last Seen:</span><span class="v">Just Now</span></div>
    <div class="row" style="top:114px"><span class="k">Project Mode</span><span class="v">Offline</span></div>
    <div class="row" style="top:163px"><span class="k">Project Info:</span><span class="v">Project 2457 Harbor</span></div>
    <div class="row" style="top:212px"><span class="k">Last Action:</span><span class="v">Cloak in<br>24 Oct, 2017 10:33 am</span></div>
  </div>
  <div class="round" style="left:135px;top:608px;background:var(--in)">in</div>
  <div class="round" style="left:194px;top:608px;background:var(--out)">out</div>
</section>

<!-- Confirmation -->
<section class="screen s4">
  <div class="map faded" role="img" aria-label="Faded street map behind the confirmation dialog"></div>
  <div class="appbar">
    <div class="status"><span class="carrier">●●●● Carrier</span><span class="time">9:41 AM</span><span class="batt">100% <i></i></span></div>
    <svg style="left:8px" width="22" height="22" viewBox="0 0 24 24" fill="none" stroke="#fff" stroke-width="2"><path d="M20 12H4M10 6l-6 6 6 6"/></svg>
    <div class="title">Attendence</div>
    <svg style="left:338px" width="22" height="22" viewBox="0 0 24 24" fill="none" stroke="#fff" stroke-width="1.8"><circle cx="12" cy="12" r="3.5"/><circle cx="12" cy="12" r="8" stroke-dasharray="4 2.3"/></svg>
  </div>
  <div class="profile"><div class="avatar" role="img" aria-label="Employee profile photo"></div><div class="name">Mara Quinlan</div><div class="code">EM12456</div></div>
  <div class="dialog">
    <h3>Confirmation</h3>
    <p>Confirm cloak in for Mara Quinlan?</p>
    <div class="dbtn cancel">Cancel</div>
    <div class="dbtn ok">Confirm</div>
  </div>
</section>

<!-- Calendar -->
<section class="screen s5">
  <div class="appbar" style="background:transparent">
    <div class="status"><span class="carrier">●●●● Carrier</span><span class="time">9:41 AM</span><span class="batt">100% <i></i></span></div>
    <svg style="left:8px" width="22" height="22" viewBox="0 0 24 24" fill="none" stroke="#fff" stroke-width="2"><path d="M20 12H4M10 6l-6 6 6 6"/></svg>
    <div class="title">Calender</div>
    <svg style="left:338px" width="22" height="22" viewBox="0 0 24 24" fill="none" stroke="#fff" stroke-width="1.8"><circle cx="12" cy="12" r="3.5"/><circle cx="12" cy="12" r="8" stroke-dasharray="4 2.3"/></svg>
  </div>
  <div class="monthbar"><span class="abs" style="left:10px">Sep</span><span class="abs" style="left:0;right:0;text-align:center">October</span><span class="abs" style="right:10px">Nov</span></div>
  <div class="cal">
    <span>S</span><span>M</span><span>T</span><span>W</span><span>T</span><span>F</span><span>S</span>
    <span>1</span><span>2</span><span>3</span><span>4</span><span>5</span><span>6</span><span class="wk">7</span>
    <span>8</span><span>9</span><span>10</span><span>11</span><span>12</span><span>13</span><span class="wk">14</span>
    <span>15</span><span>16</span><span class="sel"><b>17</b></span><span>18</span><span>19</span><span>20</span><span class="wk">21</span>
    <span>22</span><span>23</span><span>24</span><span>25</span><span>26</span><span>27</span><span class="wk">28</span>
    <span>29</span><span>30</span><span>31</span>
  </div>
  <div class="divider" style="top:437px;height:1px;background:rgba(255,255,255,.3)"></div>
  <div class="center-text" style="top:454px;color:#fff;font-size:21px;font-weight:300">17 Oct, 2017</div>
  <div class="event" style="top:499px"><div class="t">Meeting with Reyes</div><div class="s">at Tom's Bistro</div><div class="h">07:30 am</div></div>
  <div class="event" style="top:578px"><div class="t">Attendence</div><div class="s">Check-in at Office</div><div class="h">10:30 am</div></div>
</section>

<!-- Projects -->
<section class="screen s6">
  <div class="appbar">
    <div class="status"><span class="carrier">●●●● Carrier</span><span class="time">9:41 AM</span><span class="batt">100% <i></i></span></div>
    <svg style="left:10px" width="22" height="22" viewBox="0 0 24 24" fill="none" stroke="#fff" stroke-width="2"><path d="M3 6h18M3 12h18M3 18h18"/></svg>
    <div class="title">Choose Projects</div>
    <svg style="left:338px" width="22" height="22" viewBox="0 0 24 24" fill="none" stroke="#fff" stroke-width="1.8"><circle cx="12" cy="12" r="3.5"/><circle cx="12" cy="12" r="8" stroke-dasharray="4 2.3"/></svg>
  </div>
  <div class="filterbar">
    <svg class="abs" style="left:14px;top:18px" width="22" height="22" viewBox="0 0 24 24" fill="none" stroke="#fff" stroke-width="2"><path d="M3 6h18M3 10h18M3 14h14M3 18h10"/></svg>
    <span class="abs" style="left:48px;top:20px">Filter by</span>
    <svg class="abs" style="left:338px;top:18px" width="22" height="22" viewBox="0 0 24 24" fill="none" stroke="#fff" stroke-width="2"><circle cx="11" cy="11" r="7"/><path d="M16 16l5 5"/></svg>
  </div>
  <div class="acc" style="top:141px">Construction work #5489<svg width="14" height="10" viewBox="0 0 14 10" fill="none" stroke="#aaa" stroke-width="1.6"><path d="M1 8l6-6 6 6"/></svg></div>
  <div class="detail">
    <div class="line" style="top:35px"><svg viewBox="0 0 24 24"><circle cx="9" cy="8" r="4"/><path d="M2 21a7 7 0 0 1 14 0"/><path d="M16 12l2 2 4-4"/></svg><span>Construction work #2442<br>Work in Progress</span></div>
    <div class="line" style="top:99px"><svg viewBox="0 0 24 24"><circle cx="12" cy="12" r="9"/><path d="M12 7v5l3 2"/></svg><span>15 Oct, 2017 11:35am</span></div>
    <div class="line" style="top:148px"><svg viewBox="0 0 24 24"><path d="M12 21s-7-6-7-11a7 7 0 0 1 14 0c0 5-7 11-7 11z"/><circle cx="12" cy="10" r="2.5"/></svg><span>Lakeview, India</span></div>
  </div>
  <div class="acc" style="top:391px">Construction work #87955<svg width="14" height="10" viewBox="0 0 14 10" fill="none" stroke="#aaa" stroke-width="1.6"><path d="M1 2l6 6 6-6"/></svg></div>
  <div class="acc" style="top:443px">Construction work #99889<svg width="14" height="10" viewBox="0 0 14 10" fill="none" stroke="#aaa" stroke-width="1.6"><path d="M1 2l6 6 6-6"/></svg></div>
  <div class="acc" style="top:495px">Construction work #5489<svg width="14" height="10" viewBox="0 0 14 10" fill="none" stroke="#aaa" stroke-width="1.6"><path d="M1 2l6 6 6-6"/></svg></div>
  <div class="fab"><svg width="26" height="26" viewBox="0 0 24 24" fill="none" stroke="#ccc" stroke-width="1.5"><path d="M12 3v18M3 12h18"/></svg></div>
</section>

</div>
</body>
</html>
```